Design luxury business card layout
simple but slick business card layout
Professional
Rupert Calloway or Dorsan Mbeki
creative director
Whitcombe Court House
Whitcombe Court
Mayfair
London
W1K 4RT
Info@velmorabyte.com
www.velmorabyte.com
Please can all appplicants take notice of the images provided as a guide.
We will be giving feed back on a daily basis
so please check up on any updates
The reverse side of the business card will only have our logo and monogram which is one of our most important concerns . We will provide pictures as a guide which will include colour schemes etc
our Material will be similar to this

```html
<!DOCTYPE html>
<html lang="en">
<head>
<meta charset="utf-8">
<title>Velmora Byte — Business Card</title>
<link href="https://fonts.googleapis.com/css2?family=Montserrat:wght@300;400;600&display=swap" rel="stylesheet">
<style>
  :root {
    --backdrop: #2a2a2c;
    --card-red: #d9202b;
    --card-red-deep: #b5141f;
    --pattern-red: #c81a25;
    --gold: #e7c25a;
    --white: #fbeaea;
  }
  * { margin: 0; padding: 0; box-sizing: border-box; }
  html, body { width: 1200px; height: 901px; overflow: hidden; }
  body {
    background: var(--backdrop);
    font-family: "Montserrat", sans-serif;
    position: relative;
  }
  .card {
    position: absolute;
    left: 250px;
    width: 700px;
    height: 400px;
    border-radius: 22px;
    background: linear-gradient(135deg, var(--card-red) 0%, var(--card-red-deep) 100%);
    overflow: hidden;
  }
  .card-back { top: 40px; }
  .card-front { top: 461px; }

  .pattern-band {
    position: absolute;
    left: 0; right: 0;
    height: 70px;
    background: linear-gradient(90deg, var(--pattern-red), var(--card-red), var(--pattern-red));
  }
  .pattern-band.top { top: 30px; }
  .pattern-band.bottom { bottom: 30px; }

  .back-brand {
    position: absolute;
    top: 50%; left: 50%;
    transform: translate(-50%, -50%);
    display: flex; flex-direction: column; align-items: center; gap: 18px;
  }
  .brand-dot {
    width: 54px; height: 54px;
    border: 2px solid var(--gold);
    border-radius: 50%;
  }
  .brand-name {
    color: var(--white);
    font-weight: 300;
    letter-spacing: 0.35em;
    text-transform: uppercase;
  }
  .back-brand .brand-name { font-size: 20px; }

  .gold-edge {
    position: absolute; left: 0; top: 0; bottom: 0;
    width: 8px; background: var(--gold);
  }
  .front-brand { position: absolute; top: 44px; left: 50px; font-size: 18px; }

  .address {
    position: absolute; top: 110px; left: 50px;
    color: var(--gold); font-size: 14px; line-height: 1.45;
  }
  .contacts {
    position: absolute; top: 205px; left: 50px;
    list-style: none; font-size: 14px; color: var(--white); line-height: 1.5;
  }
  .contacts li { display: flex; align-items: center; gap: 10px; }
  .contacts svg { width: 14px; height: 14px; fill: var(--gold); flex: none; }

  .website {
    position: absolute; bottom: 60px; left: 50px;
    color: var(--gold); font-size: 14px; letter-spacing: 0.15em;
  }
  .person {
    position: absolute; right: 50px; bottom: 70px; text-align: right;
  }
  .person-name { color: var(--gold); font-size: 18px; font-weight: 600; }
  .person-title { color: var(--white); font-size: 14px; margin-top: 4px; }
</style>
</head>
<body>

  <section class="card card-back">
    <div class="pattern-band top" role="img" aria-label="Embossed repeating brand pattern band"></div>
    <div class="back-brand">
      <span class="brand-dot"></span>
      <span class="brand-name">Velmora Byte</span>
    </div>
    <div class="pattern-band bottom" role="img" aria-label="Embossed repeating brand pattern band"></div>
  </section>

  <section class="card card-front">
    <div class="gold-edge"></div>
    <div class="brand-name front-brand">Velmora Byte</div>

    <address class="address" style="font-style:normal">
      Whitcombe Court House<br>
      Whitcombe Court<br>
      Mayfair, London<br>
      W1K 4RT
    </address>

    <ul class="contacts">
      <li>
        <svg viewBox="0 0 24 24"><path d="M6.6 10.8a15 15 0 0 0 6.6 6.6l2.2-2.2c.3-.3.7-.4 1-.2 1.1.4 2.3.6 3.6.6.6 0 1 .4 1 1V20c0 .6-.4 1-1 1A17 17 0 0 1 3 4c0-.6.4-1 1-1h3.5c.6 0 1 .4 1 1 0 1.3.2 2.5.6 3.6.1.3 0 .7-.2 1z"/></svg>
        +44 (0) 208 614 3027
      </li>
      <li>
        <svg viewBox="0 0 24 24"><rect x="6" y="1" width="12" height="22" rx="2"/></svg>
        +44 (0) 7712 540 319
      </li>
      <li>
        <svg viewBox="0 0 24 24"><path d="M2 5h20v14H2z M2 5l10 8 10-8" /></svg>
        Info@velmorabyte.com
      </li>
    </ul>

    <div class="website">www.velmorabyte.com</div>

    <div class="person">
      <div class="person-name">Rupert Calloway</div>
      <div class="person-title">Creative Director</div>
    </div>
  </section>

</body>
</html>
```